Website design for commercial and residential security company

we're looking to see some new designs for an established company with no website.

homepage and one inner page

here is a link to the homepage content, sitemap, logo and more.
https://files.trovelink-share.net/folders/7QmzKpw3RtvxnLa9eHs2YcdJfuoPb?view=open

call to action should be Request A Quote

if you have any questions please send them to us asap

thank you

Number of Pages Required

1 page

Font styles to use
Sans Serif

```html
<!DOCTYPE html>
<html lang="en">
<head>
<meta charset="utf-8">
<title>Harbor Line Security</title>
<link href="https://fonts.googleapis.com/css2?family=Poppins:wght@300;400;500;600;700&display=swap" rel="stylesheet">
<style>
:root{
  --gold:#d1ac33;
  --ink:#1e1e1e;
  --text:#222222;
  --panel:#f2f2f2;
  --white:#ffffff;
  --foot-text:#cfcfcf;
}
*{box-sizing:border-box;margin:0;padding:0}
html,body{width:1200px;height:4242px;overflow:hidden}
body{font-family:"Poppins",sans-serif;color:var(--text);background:var(--white);position:relative}
.abs{position:absolute}
a{color:inherit;text-decoration:none}

/* hero */
.hero{position:absolute;left:0;top:0;width:1200px;height:800px;
  background:radial-gradient(ellipse at 62% 30%,rgba(120,118,110,.35),rgba(0,0,0,0) 55%),
             linear-gradient(135deg,#2a2a28 0%,#171717 45%,#0d0d0d 100%)}
.brand{position:absolute;display:flex;align-items:center;gap:10px;color:var(--white);
  font-weight:600;font-size:26px;letter-spacing:.5px}
.brand-dot{width:14px;height:14px;border-radius:50%;background:var(--gold)}
.nav a{position:absolute;top:75px;color:var(--white);font-size:14px;font-weight:500;letter-spacing:.3px}
.btn-gold{position:absolute;background:var(--gold);color:var(--white);font-weight:600;font-size:14px;
  display:flex;align-items:center;justify-content:center;letter-spacing:.5px}
.hero-sub{left:94px;top:305px;color:var(--white);font-size:18px;font-weight:300}
.hero-title{left:92px;top:345px;font-size:62px;line-height:68px;color:var(--white);font-weight:500}
.hero-title strong{color:var(--gold);font-weight:700;display:block}
.hero-rule{left:663px;top:459px;width:537px;height:2px;background:var(--gold)}
.btn-outline-light{left:94px;top:528px;width:192px;height:46px;border:2px solid rgba(255,255,255,.8);
  color:var(--white);font-size:15px;font-weight:600;display:flex;align-items:center;justify-content:center;letter-spacing:.4px}

/* about */
.about-mark{left:0;top:1318px;width:1200px;text-align:center;font-size:150px;font-weight:700;
  color:#f8f8f8;letter-spacing:2px;line-height:150px}
.gold-bar{left:204px;top:853px;width:84px;height:495px;background:var(--gold)}
.camera-photo{left:0;top:913px;width:458px;height:310px;
  background:linear-gradient(160deg,#f4f4f4 0%,#dcdcdc 60%,#c4c4c4 100%)}
.pointer-dot{left:364px;top:1092px;width:16px;height:16px;border-radius:50%;background:var(--white)}
.pointer-line{left:372px;top:1099px;width:209px;height:2px;background:var(--gold)}
.about-title{left:617px;top:965px;font-size:30px;font-weight:600;color:var(--text)}
.about-title span{color:var(--gold)}
.about-copy{left:617px;top:1026px;width:460px;font-size:15px;line-height:30px;color:var(--text)}
.btn-dark{position:absolute;background:var(--ink);color:var(--white);font-size:13px;font-weight:500;
  display:flex;align-items:center;justify-content:center}

/* solutions */
.solutions{left:0;top:1443px;width:1200px;height:2022px;background:var(--panel)}
.sec-square{position:absolute;width:66px;height:66px;background:var(--gold)}
.sec-title{position:absolute;font-size:30px;font-weight:600;color:var(--text)}
.sec-rule{position:absolute;left:535px;width:665px;height:2px;background:var(--gold)}
.photo{position:absolute}
.photo-office{left:535px;top:1681px;width:665px;height:503px;
  background:linear-gradient(180deg,#a9acaf 0%,#c7c9cb 35%,#b9ad9a 60%,#3d4a57 100%)}
.photo-room{left:535px;top:2615px;width:665px;height:504px;
  background:linear-gradient(100deg,#e9e6e0 0%,#f4f2ee 45%,#d7d3cc 75%,#b28f63 100%)}
.card{position:absolute;width:220px;height:234px;background:var(--white);
  box-shadow:0 2px 10px rgba(0,0,0,.08)}
.card-icon{position:absolute;left:18px;top:-26px;width:52px;height:52px;border-radius:50%;
  background:var(--white);display:flex;align-items:center;justify-content:center}
.card h3{position:absolute;left:13px;top:46px;font-size:20px;font-weight:500;color:var(--text)}
.card p{position:absolute;left:13px;top:92px;width:200px;font-size:11.5px;line-height:20px;color:var(--text)}
.card .btn-dark{left:13px;top:171px;width:95px;height:35px;font-size:11.5px}

/* call to action */
.cta{left:0;top:3465px;width:1200px;height:397px;background:#f6f8f8}
.photo-arch{left:708px;top:3465px;width:492px;height:397px;
  background:linear-gradient(100deg,#f6f8f8 0%,#e4eaeb 40%,#cdd6d8 70%,#b6c1c4 100%)}
.cta-title{left:94px;top:3572px;font-size:30px;font-weight:600;color:var(--text)}
.cta-copy{left:94px;top:3622px;width:480px;font-size:15px;line-height:31px}
.btn-outline-dark{position:absolute;border:1.5px solid var(--ink);color:var(--ink);font-size:14px;
  font-weight:600;display:flex;align-items:center;justify-content:center;letter-spacing:.3px}

/* footer */
.footer{left:0;top:3862px;width:1200px;height:380px;background:var(--ink)}
.foot-btn{left:970px;top:3929px;width:141px;height:45px;border:1.5px solid var(--white);color:var(--white);
  font-size:14px;font-weight:600;display:flex;align-items:center;justify-content:center}
.foot-col{position:absolute;top:4020px;color:var(--foot-text);font-size:14.5px}
.foot-col h4{font-size:14.5px;font-weight:500;color:var(--white);margin-bottom:14px;letter-spacing:.3px}
.foot-col li{list-style:none;line-height:21px;margin-bottom:14px;display:flex;align-items:center;gap:6px}
.copyright{left:112px;top:4180px;font-size:10.5px;color:#7a7a7a;letter-spacing:.2px}
</style>
</head>
<body>

<section class="hero" role="img" aria-label="Night-time photograph of a security camera mounted on a pole in front of a dark glass building"></section>

<div class="brand" style="left:90px;top:62px"><span class="brand-dot"></span>Harbor Line Security</div>
<nav class="nav">
  <a style="left:565px" href="#">ABOUT</a>
  <a style="left:663px" href="#">SOLUTIONS <svg width="10" height="8" viewBox="0 0 10 8"><path d="M1 2l4 4 4-4" stroke="#fff" stroke-width="1.6" fill="none"/></svg></a>
  <a style="left:806px" href="#">RESOURCES</a>
</nav>
<a class="btn-gold" style="left:970px;top:61px;width:141px;height:46px" href="#">CONTACT</a>

<p class="abs hero-sub">SUBTITLE HERE</p>
<h1 class="abs hero-title">Invest in <strong>securing homes.</strong></h1>
<div class="abs hero-rule"></div>
<a class="abs btn-outline-light" href="#">REQUEST &nbsp;A QUOTE</a>

<!-- about -->
<div class="abs about-mark">HARBOR LINE</div>
<div class="abs gold-bar"></div>
<div class="abs camera-photo" role="img" aria-label="Photograph of a white outdoor security camera seen from the side"></div>
<div class="abs pointer-dot"></div>
<div class="abs pointer-line"></div>
<h2 class="abs about-title">Meet our <span>company</span></h2>
<p class="abs about-copy">Lorem ipsum dolor sit amet, consectetur adipiscing elit, sed do eiusmod tempor incididunt. Lorem ipsum dolor sit amet, consectetur adipiscing elit, sed do eiusmod tempor incididunt. Lorem ipsum dolor sit amet, consectetur adipiscing elit, sed do eiusmod tempor incididunt.</p>
<a class="btn-dark" style="left:617px;top:1220px;width:129px;height:43px" href="#">LEARN MORE</a>

<!-- solutions -->
<section class="abs solutions"></section>

<div class="sec-square" style="left:94px;top:1572px"></div>
<h2 class="sec-title" style="left:118px;top:1584px">Commercial Solutions</h2>
<div class="sec-rule" style="top:1604px"></div>
<div class="photo photo-office" role="img" aria-label="Modern office building with beige panels and dark windows under a grey sky"></div>

<div class="card" style="left:94px;top:1776px">
  <div class="card-icon"><svg width="32" height="30" viewBox="0 0 32 30" fill="none" stroke="#111" stroke-width="1.8"><rect x="3" y="3" width="26" height="6" rx="2"/><path d="M6 9c0 9 4 14 10 14s10-5 10-14"/><circle cx="16" cy="16" r="5"/><circle cx="16" cy="16" r="2"/></svg></div>
  <h3>CCTV</h3>
  <p>Lorem ipsum dolor sit amet, consectetur adipiscing elit, sed do eiusmod tempor incididunt.</p>
  <a class="btn-dark" href="#">Get quote</a>
</div>
<div class="card" style="left:379px;top:1773px">
  <div class="card-icon"><svg width="34" height="32" viewBox="0 0 34 32" fill="none" stroke="#111" stroke-width="1.8"><path d="M9 24v-8a8 8 0 0 1 16 0v8"/><rect x="5" y="24" width="24" height="5"/><path d="M17 2v4M6 6l3 3M28 6l-3 3M2 15h3M29 15h3"/></svg></div>
  <h3>Alarm</h3>
  <p>Lorem ipsum dolor sit amet, consectetur adipiscing elit, sed do eiusmod tempor incididunt.</p>
  <a class="btn-dark" href="#">Get quote</a>
</div>
<div class="card" style="left:94px;top:2081px">
  <div class="card-icon"><svg width="32" height="32" viewBox="0 0 32 32" fill="none" stroke="#111" stroke-width="1.8"><rect x="3" y="3" width="26" height="26" rx="5"/><path d="M8 11h16M8 16h16M8 21h16"/><circle cx="12" cy="11" r="2" fill="#fff"/><circle cx="20" cy="16" r="2" fill="#fff"/><circle cx="13" cy="21" r="2" fill="#fff"/></svg></div>
  <h3>Access Control</h3>
  <p>Lorem ipsum dolor sit amet, consectetur adipiscing elit, sed do eiusmod tempor incididunt.</p>
  <a class="btn-dark" href="#">Get quote</a>
</div>
<div class="card" style="left:379px;top:2081px">
  <div class="card-icon"><svg width="36" height="30" viewBox="0 0 36 30" fill="none" stroke="#111" stroke-width="2" stroke-linecap="round"><path d="M2 15h5l3-8 4 18 4-22 4 20 3-12 3 6h6"/></svg></div>
  <h3>Audio/Video</h3>
  <p>Lorem ipsum dolor sit amet, consectetur adipiscing elit, sed do eiusmod tempor incididunt.</p>
  <a class="btn-dark" href="#">Get quote</a>
</div>

<div class="sec-square" style="left:94px;top:2515px"></div>
<h2 class="sec-title" style="left:118px;top:2527px">Residential Solutions</h2>
<div class="sec-rule" style="top:2547px"></div>
<div class="photo photo-room" role="img" aria-label="Bright living room with blue sofa, white chair, plants and wooden parquet floor"></div>

<div class="card" style="left:94px;top:2726px">
  <div class="card-icon"><svg width="32" height="30" viewBox="0 0 32 30" fill="none" stroke="#111" stroke-width="1.8"><rect x="3" y="3" width="26" height="6" rx="2"/><path d="M6 9c0 9 4 14 10 14s10-5 10-14"/><circle cx="16" cy="16" r="5"/><circle cx="16" cy="16" r="2"/></svg></div>
  <h3>CCTV</h3>
  <p>Lorem ipsum dolor sit amet, consectetur adipiscing elit, sed do eiusmod tempor incididunt.</p>
  <a class="btn-dark" href="#">Get quote</a>
</div>
<div class="card" style="left:379px;top:2722px">
  <div class="card-icon"><svg width="34" height="32" viewBox="0 0 34 32" fill="none" stroke="#111" stroke-width="1.8"><path d="M9 24v-8a8 8 0 0 1 16 0v8"/><rect x="5" y="24" width="24" height="5"/><path d="M17 2v4M6 6l3 3M28 6l-3 3M2 15h3M29 15h3"/></svg></div>
  <h3>Alarm</h3>
  <p>Lorem ipsum dolor sit amet, consectetur adipiscing elit, sed do eiusmod tempor incididunt.</p>
  <a class="btn-dark" href="#">Get quote</a>
</div>
<div class="card" style="left:94px;top:3029px">
  <div class="card-icon"><svg width="32" height="32" viewBox="0 0 32 32" fill="none" stroke="#111" stroke-width="1.8"><rect x="3" y="3" width="26" height="26" rx="5"/><path d="M8 11h16M8 16h16M8 21h16"/><circle cx="12" cy="11" r="2" fill="#fff"/><circle cx="20" cy="16" r="2" fill="#fff"/><circle cx="13" cy="21" r="2" fill="#fff"/></svg></div>
  <h3>Access Control</h3>
  <p>Lorem ipsum dolor sit amet, consectetur adipiscing elit, sed do eiusmod tempor incididunt.</p>
  <a class="btn-dark" href="#">Get quote</a>
</div>
<div class="card" style="left:379px;top:3029px">
  <div class="card-icon"><svg width="36" height="30" viewBox="0 0 36 30" fill="none" stroke="#111" stroke-width="2" stroke-linecap="round"><path d="M2 15h5l3-8 4 18 4-22 4 20 3-12 3 6h6"/></svg></div>
  <h3>Audio/Video</h3>
  <p>Lorem ipsum dolor sit amet, consectetur adipiscing elit, sed do eiusmod tempor incididunt.</p>
  <a class="btn-dark" href="#">Get quote</a>
</div>
<div class="card" style="left:663px;top:3029px">
  <div class="card-icon"><svg width="34" height="28" viewBox="0 0 34 28" fill="none" stroke="#111" stroke-width="3" stroke-linecap="round"><path d="M3 10a20 20 0 0 1 28 0M8 15a13 13 0 0 1 18 0M13 20a6 6 0 0 1 8 0"/><circle cx="17" cy="24" r="1.5" fill="#111"/></svg></div>
  <h3>Network Wifi</h3>
  <p>Lorem ipsum dolor sit amet, consectetur adipiscing elit, sed do eiusmod tempor incididunt.</p>
  <a class="btn-dark" href="#">Get quote</a>
</div>

<!-- call to action -->
<section class="abs cta"></section>
<div class="photo photo-arch" role="img" aria-label="White architectural ribs of a modern structure against a pale sky"></div>
<h2 class="abs cta-title">Interested in knowing more?</h2>
<p class="abs cta-copy">Lorem ipsum dolor sit amet, consectetur adipiscing elit, sed do eiusmod tempor incididunt.</p>
<a class="btn-outline-dark" style="left:94px;top:3708px;width:247px;height:45px" href="#">LEARN MORE RESOURCES</a>
<a class="btn-gold" style="left:364px;top:3708px;width:140px;height:45px" href="#">CONTACT</a>

<!-- footer -->
<footer class="abs footer"></footer>
<div class="brand" style="left:100px;top:3943px"><span class="brand-dot"></span>Harbor Line Security</div>
<a class="abs foot-btn" href="#">Request Quote</a>
<div class="foot-col" style="left:112px"><h4>ABOUT</h4><ul><li>Our Company</li><li>Members</li></ul></div>
<div class="foot-col" style="left:281px"><h4>SOLUTIONS</h4><ul><li>Commercial</li><li>Residential</li></ul></div>
<div class="foot-col" style="left:438px"><h4>RESOURCES</h4><ul><li>Packages</li><li>Specials</li></ul></div>
<div class="foot-col" style="left:589px"><h4>CONTACT</h4><ul>
  <li><svg width="13" height="10" viewBox="0 0 13 10" fill="none" stroke="#cfcfcf" stroke-width="1.2"><rect x=".6" y=".6" width="11.8" height="8.8"/><path d="M.6 .6l5.9 5 5.9-5"/></svg>info@harborline-security.com</li>
  <li><svg width="12" height="12" viewBox="0 0 12 12"><path d="M2.5 1l2 2.4-1.2 1.4a7 7 0 0 0 3.9 3.9l1.4-1.2 2.4 2-1.4 1.5C5.5 10.6 1.4 6.5 1 2.4z" fill="#cfcfcf"/></svg>555 010 2040</li>
</ul></div>
<p class="abs copyright">2020 HARBOR LINE SECURITY. ALL RIGHTS RESERVED.</p>

</body>
</html>
```